New business card for civil engineering company - "Keystone Audit"

We need a business card designed for our new structural engineering company.

The company name is "Keystone Audit" logo files attached.

We would like the following:
* Two-sided card
* Simple design

Information to be placed on the card:
Name - Marcus Dellow
Job Title - Director / Structural Engineer
Credentials - BEng(Hons), CPEng, CMengNZ, IntPE(NZ)
Email - marcus.dellow@keystoneaudit.co.nz
mobile - 0219364058
website - www.keystoneaudit.co.nz

```html
<!DOCTYPE html>
<html lang="en">
<head>
<meta charset="utf-8">
<title>Keystone Audit – Business Card</title>
<link href="https://fonts.googleapis.com/css2?family=Arimo:wght@400;700&family=Exo+2:wght@500&display=swap" rel="stylesheet">
<style>
  :root {
    --backdrop: #e9e9e9;
    --navy: #123a66;
    --accent: #3b7cc4;
    --paper: #ececec;
    --ink: #555555;
    --ink-dark: #333333;
    --white: #ffffff;
  }
  * { margin: 0; padding: 0; box-sizing: border-box; }
  html, body { width: 1200px; height: 1200px; overflow: hidden; }
  body { background: var(--backdrop); position: relative; font-family: "Arimo", Arial, sans-serif; }

  .card { position: absolute; left: 227px; width: 746px; height: 426px; }

  /* Front */
  .card-front { top: 135px; background: var(--navy); }
  .front-brand { position: absolute; left: 0; right: 0; top: 296px; text-align: center; }
  .brand-name {
    font-family: "Exo 2", sans-serif; font-weight: 500;
    color: var(--white); font-size: 30px; letter-spacing: 4px; text-transform: uppercase;
    line-height: 1;
  }

  /* Back */
  .card-back { top: 639px; background: var(--paper); }
  .edge-band { position: absolute; left: 0; width: 19px; background: var(--navy); }
  .edge-band.top { top: 0; height: 106px; }
  .edge-band.middle { top: 110px; height: 69px; background: var(--accent); }
  .edge-band.bottom { top: 182px; height: 244px; }

  .person { position: absolute; left: 65px; top: 105px; }
  .person-name { color: var(--accent); font-size: 29px; font-weight: 700; letter-spacing: -0.3px; line-height: 1; }
  .person-name .surname { font-weight: 400; }
  .person-role, .person-credentials { color: var(--ink); font-size: 17px; line-height: 22px; }
  .person-role { margin-top: 4px; }

  .back-brand { position: absolute; left: 490px; width: 220px; top: 213px; text-align: right; }
  .back-brand .brand-name { color: var(--ink-dark); font-size: 19px; letter-spacing: 2.5px; }

  .contact { position: absolute; left: 65px; display: flex; align-items: center; gap: 9px;
    color: var(--ink); font-size: 17px; }
  .contact svg { width: 16px; height: 16px; flex: none; }
  .contact.phone { top: 286px; }
  .contact.email { top: 310px; }
  .contact.web { top: 356px; }
  .divider { position: absolute; left: 65px; width: 628px; top: 346px; height: 1.5px; background: var(--accent); }
</style>
</head>
<body>
  <section class="card card-front">
    <div class="front-brand">
      <div class="brand-name">Keystone Audit</div>
    </div>
  </section>

  <section class="card card-back">
    <div class="edge-band top"></div>
    <div class="edge-band middle"></div>
    <div class="edge-band bottom"></div>

    <div class="person">
      <div class="person-name">MARCUS <span class="surname">DELLOW</span></div>
      <div class="person-role">Director / Structural Engineer</div>
      <div class="person-credentials">BEng(Hons), CPEng, CMengNZ, IntPE(NZ)</div>
    </div>

    <div class="back-brand">
      <div class="brand-name">Keystone Audit</div>
    </div>

    <div class="contact phone">
      <svg viewBox="0 0 16 16" fill="none" stroke="#3b7cc4" stroke-width="1.4"><rect x="4" y="1" width="8" height="14" rx="1.5"/><line x1="7" y1="12.5" x2="9" y2="12.5"/></svg>
      <span>021-936-4058</span>
    </div>
    <div class="contact email">
      <svg viewBox="0 0 16 16" fill="none" stroke="#3b7cc4" stroke-width="1.3"><rect x="1.5" y="3.5" width="13" height="9"/><path d="M1.5 3.5 8 9l6.5-5.5M1.5 12.5l5-4.5M14.5 12.5l-5-4.5"/></svg>
      <span>marcus.dellow@keystoneaudit.co.nz</span>
    </div>
    <div class="divider"></div>
    <div class="contact web">
      <svg viewBox="0 0 16 16" fill="none" stroke="#3b7cc4" stroke-width="1.2"><circle cx="8" cy="8" r="6.5"/><ellipse cx="8" cy="8" rx="2.8" ry="6.5"/><path d="M1.5 8h13M2.5 4.8h11M2.5 11.2h11"/></svg>
      <span>www.keystoneaudit.co.nz</span>
    </div>
  </section>
</body>
</html>
```